Business card

We need a business card design for our company based in Auckland , New Zealand called 'Kestrel + Design Ltd'. We provide architectural services. We would like to see designs that use the max. three colours (such as white, black, grey) The final design should communicate financial safety and growth."
Also I will provide our company logo. I would like to the logo to be embeded onto our business card.

Target Market(s)

new residential house, alteration & addition & light commericila design & drafting service

Industry/Entity Type

Architecture

Contact Information for Business Card

Company name: kestrel + design Ltd.
Name: Mark Telford
Job title: architectural designer & Design RQC
email address: mark@kdstudio.co.nz
mobile number: 02 5319 6620
web site: www.kdstudio.co.nz

Requirements
Must have
• My project must have..
• - embeded logo (attached company logo)
• I don't have a bigger version for our company logo, but I have one old one, so you can remove the word from it)
• - insert the attached small PDGQ logo & RQC logo
• - creative, simple and clear business card.
• - Max. three colours
Nice to have
• - Here are the samples I would like to share with you: http://www.velmorindex.com/blog/minimalistic-business-card-designs/
• I would like to have my business card like one of the creation.
Should not have
• TBA

```html
<!DOCTYPE html>
<html lang="en">
<head>
<meta charset="utf-8">
<title>Kestrel + Design Ltd. — Business Card</title>
<link href="https://fonts.googleapis.com/css2?family=Fira+Sans:wght@300;400;500&display=swap" rel="stylesheet">
<style>
  :root {
    --ink: #111111;
    --paper: #ffffff;
    --grey: #7a7a7a;
    --grey-dark: #5e5e5e;
    --backdrop: #e4e4e4;
  }
  * { margin: 0; padding: 0; box-sizing: border-box; }
  html, body { width: 960px; height: 1200px; overflow: hidden; }
  body {
    background: var(--backdrop);
    font-family: "Fira Sans", Arial, sans-serif;
    position: relative;
  }
  .card {
    position: absolute;
    left: 80px;
    width: 800px;
    height: 444px;
    box-shadow: 0 6px 18px rgba(0,0,0,0.15);
    overflow: hidden;
  }
  .card--front { top: 104px; background: var(--paper); color: var(--ink); }
  .card--back  { top: 652px; background: var(--ink); }

  /* front */
  .badges {
    position: absolute; top: 38px; right: 56px;
    display: flex; align-items: center; gap: 18px;
  }
  .badge-round { width: 66px; height: 66px; border-radius: 50%; background: var(--ink); }
  .badge-square { width: 56px; height: 56px; background: var(--grey-dark); }
  .divider {
    position: absolute; top: 152px; left: 380px; right: 0;
    height: 2px; background: var(--ink);
  }
  .wordmark {
    position: absolute; top: 196px; left: 64px;
    display: flex; align-items: center; gap: 10px;
    font-weight: 500; font-size: 24px; line-height: 1.1; color: var(--ink);
    white-space: nowrap;
  }
  .wordmark__square { width: 14px; height: 14px; background: var(--ink); }
  .contact { position: absolute; top: 268px; left: 64px; }
  .contact__name { font-weight: 400; font-size: 26px; line-height: 1.1; }
  .contact__role { font-weight: 300; font-size: 17px; color: var(--grey); margin-bottom: 14px; }
  .contact__detail { font-weight: 400; font-size: 17px; line-height: 1.35; }

  /* back */
  .back-mark {
    position: absolute; top: 0; left: 0; right: 0; bottom: 0;
    display: flex; align-items: center; justify-content: center; gap: 22px;
    font-weight: 500; font-size: 58px; line-height: 1;
    color: var(--grey-dark); white-space: nowrap;
  }
  .back-mark__square { width: 30px; height: 30px; background: var(--grey-dark); }
</style>
</head>
<body>
  <section class="card card--front" aria-label="Card front">
    <div class="badges">
      <div class="badge-round" role="img" aria-label="Licensed practitioner badge"></div>
      <div class="badge-square" role="img" aria-label="PDGQ professional member badge"></div>
    </div>
    <div class="divider"></div>
    <div class="wordmark">
      <span class="wordmark__square"></span>
      <span>Kestrel + Design Ltd.</span>
    </div>
    <div class="contact">
      <p class="contact__name">Mark Telford</p>
      <p class="contact__role">Architectural designer &amp; Design RQC</p>
      <p class="contact__detail">02 5319 6620</p>
      <p class="contact__detail">mark@kdstudio.co.nz</p>
      <p class="contact__detail">www.kdstudio.co.nz</p>
    </div>
  </section>

  <section class="card card--back" aria-label="Card back">
    <div class="back-mark">
      <span class="back-mark__square"></span>
      <span>Kestrel + Design Ltd.</span>
    </div>
  </section>
</body>
</html>
```